business card double side design

We need a business card design for our company BRIGHTlearn. DOUBLE SIDED. We provide continuing education programs & courses across North America. Our website is www.brightlearn-example.com - please use the grey pinstrip concept as part of the design. Compliment the branding that is occuring on that site!
Please use pantones daa520 and 3f3151. Verdana for text. I have attached our logo.
I would like the logo & website address www.BRIGHTlearn-example.com on the front of the card, all other info on the backside. The final design should communicate authority and credibility.

Industry/Entity Type

Professional Service

Font styles to use
Other font styles liked:
• verdanda

Requirements
Must have
• pantones daa520 and 3f3151. Verdana for text.
• must compliment the branding occuring on the www.BRIGHTlearn-example.com

```html
<!DOCTYPE html>
<html lang="en">
<head>
<meta charset="utf-8">
<title>BRIGHTlearn business card</title>
<link href="https://fonts.googleapis.com/css2?family=Open+Sans:wght@400;600;700&display=swap" rel="stylesheet">
<style>
  :root {
    --gold: #daa520;
    --purple: #3f3151;
    --card: #f6f6f6;
    --ink: #1f1f1f;
    --backdrop: #cbcbcb;
  }
  * { box-sizing: border-box; margin: 0; padding: 0; }
  html, body { width: 1200px; height: 1005px; overflow: hidden; }
  body {
    background: var(--backdrop);
    font-family: "Open Sans", Verdana, sans-serif;
    color: var(--ink);
    display: flex;
    flex-direction: column;
    align-items: center;
    justify-content: center;
    gap: 50px;
  }
  .card {
    position: relative;
    width: 700px;
    height: 400px;
    background: var(--card);
    box-shadow: 0 6px 14px rgba(0,0,0,0.25);
    overflow: hidden;
  }
  .brand {
    display: flex;
    align-items: center;
    gap: 18px;
  }
  .brand-dot {
    border-radius: 50%;
    background: var(--gold);
  }
  .brand-name {
    font-weight: 700;
    color: var(--purple);
    letter-spacing: 0.5px;
  }

  /* Front */
  .card-front .brand {
    position: absolute;
    left: 0; right: 0; top: 120px;
    justify-content: center;
  }
  .card-front .brand-dot { width: 120px; height: 120px; }
  .card-front .brand-name { font-size: 56px; }
  .front-url {
    position: absolute;
    left: 0; right: 0; bottom: 78px;
    display: flex;
    align-items: center;
    justify-content: center;
    gap: 14px;
    font-size: 17px;
  }
  .front-url::before, .front-url::after {
    content: "";
    width: 50px; height: 3px;
    background: var(--purple);
  }
  .front-band {
    position: absolute;
    left: 0; right: 0; bottom: 0;
    height: 42px;
    background: var(--purple);
    border-top: 4px solid var(--gold);
  }

  /* Back */
  .back-wave { position: absolute; inset: 0; }
  .card-back .brand {
    position: absolute;
    left: 58px; top: 44px;
  }
  .card-back .brand-dot { width: 92px; height: 92px; }
  .card-back .brand-name { font-size: 38px; }
  .social {
    position: absolute;
    right: 60px; top: 32px;
    display: flex; gap: 5px;
  }
  .social span {
    width: 22px; height: 22px;
    border-radius: 3px;
    background: var(--purple);
  }
  .contact {
    position: absolute;
    left: 58px; top: 168px;
    list-style: none;
    font-size: 15px;
    line-height: 24px;
  }
  .contact li { display: flex; align-items: center; gap: 14px; }
  .contact svg { width: 16px; height: 16px; flex: none; }
  .person {
    position: absolute;
    right: 40px; bottom: 104px;
    text-align: right;
    color: #fff;
  }
  .person-name { font-size: 26px; font-weight: 600; line-height: 1.15; }
  .person-role { font-size: 15px; }
</style>
</head>
<body>

  <section class="card card-front">
    <div class="brand">
      <span class="brand-dot"></span>
      <span class="brand-name">BRIGHTlearn</span>
    </div>
    <p class="front-url">www.BRIGHTlearn-example.com</p>
    <div class="front-band"></div>
  </section>

  <section class="card card-back">
    <svg class="back-wave" viewBox="0 0 700 400" preserveAspectRatio="none" aria-hidden="true">
      <path d="M0 352 C200 345 330 340 420 250 C500 170 600 130 700 118 L700 400 L0 400 Z" fill="#3f3151"/>
      <path d="M0 336 C200 329 330 324 414 236 C496 154 600 112 700 100" fill="none" stroke="#daa520" stroke-width="7"/>
      <path d="M110 343 C260 340 350 328 424 256" fill="none" stroke="#daa520" stroke-width="3"/>
    </svg>

    <div class="brand">
      <span class="brand-dot"></span>
      <span class="brand-name">BRIGHTlearn</span>
    </div>

    <div class="social"><span></span><span></span><span></span></div>

    <ul class="contact">
      <li>
        <svg viewBox="0 0 16 16"><path d="M3 1l3 3-2 2c1 2 3 4 5 5l2-2 3 3-2 3C7 15 1 9 1 3z" fill="#daa520"/></svg>
        555.014.2290
      </li>
      <li>
        <svg viewBox="0 0 16 16"><path d="M1 3h14v10H1z M2 4l6 5 6-5" fill="none" stroke="#daa520" stroke-width="1.6"/></svg>
        dana@BRIGHTlearn-example.com
      </li>
      <li>
        <svg viewBox="0 0 16 16"><circle cx="8" cy="8" r="6.5" fill="none" stroke="#daa520" stroke-width="1.6"/><path d="M1.5 8h13M8 1.5c-3 3-3 10 0 13M8 1.5c3 3 3 10 0 13" fill="none" stroke="#daa520" stroke-width="1.2"/></svg>
        www.BRIGHTlearn-example.com
      </li>
      <li>Suite 140, 88 Maple Crest Road</li>
      <li>Lakeview, Alberta</li>
    </ul>

    <div class="person">
      <p class="person-name">Dana Whitlock</p>
      <p class="person-role">Technical Support</p>
    </div>
  </section>

</body>
</html>
```